Kovalen Spinal Care and Performance

We need new business cards, something more modern, clean. On the back of the card maybe a quote. The Dr. likes, “The doctor of the future will give no medicine, but will interest his patient in the care of the human frame, in diet and in the cause and prevention of disease.” - Walter Brisby. We are open to other suggestions. We are a chiropractic office.

```html
<!DOCTYPE html>
<html lang="en">
<head>
<meta charset="utf-8">
<title>Kovalen Spinal Care and Performance – Business Card</title>
<link href="https://fonts.googleapis.com/css2?family=Lato:wght@400;700;900&family=Italianno&display=swap" rel="stylesheet">
<style>
  :root {
    --stage: #cfcfcf;
    --card-white: #f4f4f4;
    --purple: #4b1f52;
    --purple-deep: #2a1530;
    --ink: #1f1a22;
    --green: #8fae2f;
    --olive: #55662a;
    --back-top: #4a1e50;
    --back-bottom: #121014;
  }
  * { box-sizing: border-box; margin: 0; padding: 0; }
  html, body { width: 1200px; height: 675px; overflow: hidden; }
  body {
    background: var(--stage);
    font-family: "Lato", sans-serif;
    display: flex;
    align-items: center;
    justify-content: center;
    gap: 40px;
  }
  .card {
    position: relative;
    width: 540px;
    height: 309px;
    overflow: hidden;
    box-shadow: 0 6px 18px rgba(0,0,0,0.25);
  }

  /* Front */
  .card-front { background: linear-gradient(160deg, #ffffff 0%, var(--card-white) 100%); }
  .brand {
    position: absolute;
    left: 28px; top: 104px;
    width: 200px;
    display: flex; align-items: center; gap: 10px;
  }
  .brand-mark {
    flex: none;
    width: 16px; height: 16px; border-radius: 50%;
    background: var(--green);
  }
  .brand-name {
    color: var(--purple);
    font-weight: 700;
    font-size: 16px;
    line-height: 1.25;
  }
  .divider {
    position: absolute;
    left: 246px; top: 62px;
    width: 1.5px; height: 168px;
    background: var(--olive);
  }
  .contact {
    position: absolute;
    left: 266px; top: 64px;
    color: var(--ink);
  }
  .contact-name {
    color: var(--purple);
    font-weight: 900;
    font-size: 17px;
    letter-spacing: 0.5px;
    text-transform: uppercase;
  }
  .contact-role { font-size: 12px; color: #444; margin-top: 1px; }
  .contact-address { font-size: 12px; line-height: 1.35; margin-top: 10px; }
  .contact-list { list-style: none; margin-top: 8px; font-size: 12px; }
  .contact-list li { display: flex; align-items: center; gap: 7px; line-height: 1.45; }
  .contact-list svg { width: 11px; height: 11px; fill: var(--purple); flex: none; }
  .swoosh { position: absolute; left: 0; bottom: 0; width: 540px; height: 309px; }

  /* Back */
  .card-back {
    background: linear-gradient(180deg, var(--back-top) 0%, #2b1630 45%, var(--back-bottom) 100%);
    display: flex; align-items: center; justify-content: center;
  }
  .quote {
    width: 440px;
    color: #f3eef4;
    font-family: "Italianno", cursive;
    font-size: 25px;
    line-height: 1.15;
    text-align: center;
  }
</style>
</head>
<body>

  <section class="card card-front">
    <div class="brand">
      <span class="brand-mark"></span>
      <span class="brand-name">Kovalen Spinal Care<br>and Performance</span>
    </div>

    <div class="divider"></div>

    <div class="contact">
      <p class="contact-name">Daniel Marlowe</p>
      <p class="contact-role">Owner</p>
      <p class="contact-address">4120 Larkfield Road, Ashbury<br>NC 27, United States</p>
      <ul class="contact-list">
        <li><svg viewBox="0 0 24 24"><path d="M6.6 10.8a15.2 15.2 0 0 0 6.6 6.6l2.2-2.2a1 1 0 0 1 1-.25 11.4 11.4 0 0 0 3.6.57 1 1 0 0 1 1 1V20a1 1 0 0 1-1 1A17 17 0 0 1 3 4a1 1 0 0 1 1-1h3.5a1 1 0 0 1 1 1c0 1.25.2 2.45.57 3.57a1 1 0 0 1-.25 1z"/></svg>000-000-000-000</li>
        <li><svg viewBox="0 0 24 24"><path d="M6 2h12v5H6zM4 8h16a2 2 0 0 1 2 2v6h-4v6H6v-6H2v-6a2 2 0 0 1 2-2zm4 8v4h8v-4z"/></svg>000-000-000-000</li>
        <li><svg viewBox="0 0 24 24"><path d="M2 5h20v14H2zm2 2v.4l8 5.2 8-5.2V7z"/></svg>info@websitename.com</li>
        <li><svg viewBox="0 0 24 24"><path d="M12 2a10 10 0 1 0 0 20 10 10 0 0 0 0-20zm6.9 6h-3a15 15 0 0 0-1.3-3.9A8 8 0 0 1 18.9 8zM12 4c.9 1.2 1.6 2.5 2 4h-4c.4-1.5 1.1-2.8 2-4zM4.3 14a8 8 0 0 1 0-4h3.4a16 16 0 0 0 0 4zm.8 2h3a15 15 0 0 0 1.3 3.9A8 8 0 0 1 5.1 16zm3-8h-3a8 8 0 0 1 4.3-3.9A15 15 0 0 0 8.1 8zM12 20c-.9-1.2-1.6-2.5-2-4h4c-.4 1.5-1.1 2.8-2 4zm2.3-6H9.7a14 14 0 0 1 0-4h4.6a14 14 0 0 1 0 4zm.3 5.9a15 15 0 0 0 1.3-3.9h3a8 8 0 0 1-4.3 3.9zm1.7-5.9a16 16 0 0 0 0-4h3.4a8 8 0 0 1 0 4z"/></svg>www.websitename.com</li>
      </ul>
    </div>

    <svg class="swoosh" viewBox="0 0 540 309" aria-hidden="true">
      <defs>
        <linearGradient id="band-green" x1="0" x2="1" y1="0" y2="0">
          <stop offset="0" stop-color="#4d5e27"/>
          <stop offset="1" stop-color="#9bbb32"/>
        </linearGradient>
      </defs>
      <path d="M225 309 C320 272 440 264 540 272 L540 309 Z" fill="url(#band-green)"/>
      <path d="M200 309 C290 256 400 250 470 262 C390 260 300 272 238 309 Z" fill="var(--purple)"/>
    </svg>
  </section>

  <section class="card card-back">
    <p class="quote">“The doctor of the future will give no medicine, but will interest his patient in the care of the human frame, in diet and in the cause and prevention of disease.” - Walter Brisby.</p>
  </section>

</body>
</html>
```